Need Stunning Website for Talent Acquisition (Recruiting) Agency

Hello, I am seeking a very professional, high-quality website that reflects our Talent Acquisition agency, Cobalt Kin. Our agency slogan is "Talent Acquisition. Differently." We are in fact different - we are a full service agency that provides services most others do not, and our website needs to immediately reflect that something is different about us when they visit our site.

This contest is to do complete website design and coding, including all graphics, features, plugins, and design elements. The graphics are very important on the site and must be of the highest professional quality. One critical aspect is that the imagery must convey that we serve clients in a variety of industries, including business, healthcare, churches and religious organizations, non-profits, manufacturing, retail, and more. We recruit for both professional level positions (e.g. CEO, COO, Pastor), as well as entry level (e.g. secretary, caregiver, factory worker).
The following pages should be designed:
Home Page - a captivating home page that immediately tells our brand story, what makes us different, and the value that we bring to the table.
Client Services Page - a page that talks more about the services we provide and why we produce better results. This page will cover the 5 C's in greater detail as well as all the things that make us different.
Industries - The industries we serve
Request Services - a page where clients can submit details about a job they would like us to recruit for, including attaching a job description if they have one
Candidates Page - a simple page that encourages prospective candidates to submit their resume for review
About Us - Common about us page
Blog - Common blog page
Contact Us - a contact page for general inquiries
The website must be built in an ultra-SEO friendly manner and optimized for speed and performance. As mentioned above, you will be responsible for providing all graphics for the site (copyright compliant).
The website will need to be compatible with Elementor Pro (I have subscription) and Yoast SEO. It needs to be designed on a high-quality wordpress theme that receives regular updates. It also needs instant chat messaging feature. Would like a traditional menu bar at the top of the page (not a fan of menu's that are hidden or put on the side of the page).

Please, please, please - - do NOT waste my time with generic/stock templates, low-quality graphics, etc. We are a PREMIUM agency and our website needs to reflect that.

In the future we will add a job board - I do not want that initially - but will want the option to add it later.

Must also have the ability to upload documents /attachments on the contact page/form.

It probably goes without saying, but the page must be fully responsive - suitable to work on all device types.

Target Market(s)

Businesses

Industry/Entity Type

Talent Acquisition (Recruiting) Agency

Coding

Coded - Design and coding required

Number of Pages Required

5+ page

Requirements
Must have
• Please see brief
Should not have
• No generic template/stock website or graphics - must have PREMIUM feel.

```html
<!DOCTYPE html>
<html lang="en">
<head>
<meta charset="utf-8">
<title>Cobalt Kin — Talent Acquisition. Differently.</title>
<link href="https://fonts.googleapis.com/css2?family=Montserrat:wght@400;500;600;700;800&family=Dancing+Script:wght@500&display=swap" rel="stylesheet">
<style>
:root{
  --orange:#f9a61b;
  --navy:#141b4d;
  --ink:#1b1b2a;
  --grey:#6c6c78;
  --tile:#ececec;
  --black:#050505;
  --white:#ffffff;
  --cream:#efe3cf;
}
*{box-sizing:border-box;margin:0;padding:0}
html,body{width:1200px;height:3552px;overflow:hidden}
body{position:relative;background:var(--white);font-family:"Montserrat",sans-serif;color:var(--ink)}
.abs{position:absolute}
.brand{font-family:"Montserrat",sans-serif;font-weight:800;font-size:22px;color:var(--navy);display:flex;align-items:center;gap:8px;letter-spacing:-.3px}
.brand .dot{width:12px;height:12px;background:var(--orange);border-radius:50%}
.brand.light{color:var(--white)}

/* header */
.site-header{left:0;top:0;width:1200px;height:48px;background:var(--white);display:flex;align-items:center;padding:0 40px;justify-content:space-between}
.main-nav{display:flex;gap:34px;font-size:11px;font-weight:600;color:var(--navy);letter-spacing:.4px}
.main-nav a{text-decoration:none;color:inherit;padding-bottom:4px}
.main-nav a.active{color:var(--orange);border-bottom:2px solid var(--orange)}

/* hero */
.hero-half{top:48px;width:600px;height:512px;color:var(--white);text-align:center;padding-top:130px}
.hero-candidate{left:0;background:var(--orange)}
.hero-employer{left:600px;background:var(--navy)}
.hero-kicker{font-family:"Dancing Script",cursive;font-size:30px}
.hero-title{font-weight:800;font-size:54px;line-height:58px;letter-spacing:1px;margin-top:8px}
.hero-text{font-size:12px;line-height:17px;width:360px;margin:18px auto 0}
.btn-outline{display:inline-block;margin-top:28px;border:2px solid var(--white);padding:11px 26px;font-size:12px;font-weight:700;letter-spacing:.8px;color:var(--white)}
.hero-employer .btn-outline{border-color:var(--white)}

/* about */
.section-title{font-weight:800;color:var(--navy);letter-spacing:.5px}
.about-title{left:168px;top:682px;width:380px;font-size:32px;line-height:40px}
.about-text{left:600px;top:660px;width:440px;font-size:14px;line-height:22px;color:var(--grey)}
.link-more{font-size:14px;font-weight:700;color:var(--orange)}
.about-photo{left:600px;top:860px;width:432px;height:280px;background:linear-gradient(135deg,#dfe3ea,#8a93a6 60%,#3b4258)}
.proud-box{left:168px;top:1000px;width:552px;height:260px;background:var(--navy);color:var(--white);padding:56px 40px;font-weight:800;font-size:29px;line-height:40px}

/* career */
.career{left:0;top:1300px;width:1200px;height:640px;background:linear-gradient(180deg,#f4ecdd,#e9dcc4 55%,#e1cfae)}
.center-block{width:1200px;left:0;text-align:center}
.career-title{font-size:26px}
.lead{font-size:13px;line-height:20px;color:var(--grey);width:560px;margin:0 auto}
.step-card{top:1572px;width:224px;height:260px;text-align:center;padding:30px 20px}
.step-card.dark{background:var(--navy);color:var(--white)}
.step-card.light{background:var(--white);border:3px solid var(--orange);color:var(--ink)}
.step-card h3{font-size:13px;font-weight:700;color:var(--orange);margin-top:18px}
.step-card p{font-size:12px;line-height:18px;margin-top:8px}
.step-card .btn-small{display:inline-block;margin-top:16px;font-size:10px;font-weight:600;padding:7px 16px;border:1px solid currentColor}

/* positions */
.positions-title{font-size:26px}
.industry-tile{width:140px;height:148px;background:var(--tile);display:flex;flex-direction:column;align-items:center;justify-content:center;gap:14px;font-size:13px;font-weight:700;color:var(--navy);letter-spacing:.4px}
.industry-bar{width:140px;height:6px;background:var(--orange)}

/* people */
.people-photo{left:112px;top:2600px;width:976px;height:500px;background:linear-gradient(90deg,#2e3238,#6d737c 45%,#a8adb3)}
.people-box{left:640px;top:2660px;width:380px;height:280px;background:var(--orange);color:var(--white);padding:40px 36px}
.people-box h2{font-size:34px;font-weight:800}
.people-box p{font-size:13px;line-height:20px;margin-top:14px}
.btn-white{display:inline-block;margin-top:22px;background:var(--white);color:var(--orange);font-size:11px;font-weight:700;padding:10px 22px}

/* footer */
.site-footer{left:0;top:3140px;width:1200px;height:412px;background:var(--black);color:var(--white)}
.f-head{font-size:20px;font-weight:700;color:var(--orange)}
.f-list{list-style:none;font-size:14px;line-height:30px;margin-top:14px}
.f-text{font-size:14px;line-height:24px}
.footer-bottom{left:0;top:3480px;width:1200px;height:72px;border-top:1px solid #222;display:flex;align-items:center;justify-content:space-between;padding:0 40px 0 40px;font-size:12px;font-weight:600}
.socials{display:flex;gap:8px}
.socials span{width:26px;height:26px;background:#3b5bdb;display:block}
</style>
</head>
<body>

<header class="site-header abs">
  <div class="brand"><span class="dot"></span>Cobalt Kin</div>
  <nav class="main-nav">
    <a class="active" href="#">HOME</a><a href="#">CLIENT SERVICES</a><a href="#">INDUSTRIES</a><a href="#">REQUEST SERVICES</a><a href="#">CANDIDATES</a><a href="#">BLOG</a>
  </nav>
</header>

<section class="hero-half hero-candidate abs">
  <div class="hero-kicker">I'm a candidate</div>
  <h1 class="hero-title">LOOKING<br>FOR A JOB</h1>
  <p class="hero-text">Lorem Ipsum is simply dummy text of the printing and typesetting industry. Lorem Ipsum has been the standard dummy text.</p>
  <span class="btn-outline">APPLY NOW</span>
</section>
<section class="hero-half hero-employer abs">
  <div class="hero-kicker">I'm a employer</div>
  <h1 class="hero-title">MANAGING<br>A WORKPLACE</h1>
  <p class="hero-text">Lorem Ipsum is simply dummy text of the printing and typesetting industry. Lorem Ipsum has been the standard dummy text.</p>
  <span class="btn-outline">OUR SERVICES</span>
</section>

<div class="brand abs" style="left:168px;top:616px">Cobalt Kin</div>
<h2 class="section-title about-title abs">WE'RE RAISING THE BAR FOR WORKFORCE MANAGEMENT.</h2>
<p class="about-text abs">Lorem Ipsum is simply dummy text of the printing and typesetting industry. Lorem Ipsum has been the industry's standard dummy text ever since the 1500s, when an unknown printer took a galley of type and scrambled it to make a type specimen book. It has survived not only five centuries.</p>
<span class="link-more abs" style="left:928px;top:812px">About Us &gt;</span>
<div class="about-photo abs" role="img" aria-label="Photo of business people shaking hands across a meeting table"></div>
<div class="proud-box abs">WE ARE PROUD TO OFFER TOP RANGE OF COMPREHENSIVE EMPLOYMENT SERVICES AND ASSISTANCE.</div>
<span class="link-more abs" style="left:928px;top:1250px">Read More &gt;</span>

<section class="career abs" role="img" aria-label="Faded photo of a desk with coffee and office items"></section>
<div class="center-block abs" style="top:1344px;display:flex;justify-content:center"><div class="brand"><span class="dot"></span>Cobalt Kin</div></div>
<h2 class="center-block section-title career-title abs" style="top:1432px">HOW TO BUILD YOUR CAREER?</h2>
<p class="center-block abs" style="top:1484px"><span class="lead" style="display:block">Lorem Ipsum is simply dummy text of the printing and typesetting industry. Lorem Ipsum has been the industry's standard dummy text ever since the 1500s.</span></p>

<div class="step-card dark abs" style="left:252px">
  <svg width="40" height="44" viewBox="0 0 40 44" fill="none" stroke="#fff" stroke-width="2.5"><rect x="6" y="4" width="28" height="36" rx="2"/><line x1="12" y1="14" x2="28" y2="14"/><line x1="12" y1="22" x2="28" y2="22"/><line x1="12" y1="30" x2="22" y2="30"/></svg>
  <h3>Sign up and Set up your Profile</h3>
  <p>Lorem Ipsum is simply dummy text of the printing and typesetting industry.</p>
  <span class="btn-small">Sign Up</span>
</div>
<div class="step-card light abs" style="left:488px">
  <svg width="40" height="44" viewBox="0 0 40 44" fill="none" stroke="#f9a61b" stroke-width="2.5"><rect x="6" y="4" width="28" height="36" rx="2"/><path d="M12 22l6 6 10-12"/></svg>
  <h3>Create a CV</h3>
  <p>Lorem Ipsum is simply dummy text of the printing and typesetting industry.</p>
  <span class="btn-small" style="color:var(--navy)">Submit Your CV</span>
</div>
<div class="step-card dark abs" style="left:724px">
  <svg width="44" height="44" viewBox="0 0 44 44" fill="none" stroke="#fff" stroke-width="2.5"><rect x="4" y="14" width="36" height="24" rx="2"/><path d="M15 14v-5h14v5"/><line x1="4" y1="24" x2="40" y2="24"/></svg>
  <h3>Apply &amp; Get Applied</h3>
  <p>Lorem Ipsum is simply dummy text of the printing and typesetting industry.</p>
  <span class="btn-small">Submit Your CV</span>
</div>

<div class="center-block abs" style="top:2000px;display:flex;justify-content:center"><div class="brand"><span class="dot"></span>Cobalt Kin</div></div>
<h2 class="center-block section-title positions-title abs" style="top:2068px">ALL POSITIONS THAT WE DEALS WITH</h2>
<p class="center-block abs" style="top:2114px"><span class="lead" style="display:block">Lorem Ipsum is simply dummy text of the printing and typesetting industry. Lorem Ipsum has been the industry's standard dummy text ever since the 1500s.</span></p>

<!-- industry grid -->
<div class="industry-tile abs" style="left:280px;top:2212px"><svg width="40" height="40" viewBox="0 0 40 40" fill="none" stroke="#141b4d" stroke-width="2.5"><rect x="6" y="8" width="16" height="28"/><rect x="22" y="18" width="12" height="18"/><line x1="11" y1="15" x2="17" y2="15"/><line x1="11" y1="22" x2="17" y2="22"/></svg>INDUSTRIES</div>
<div class="industry-tile abs" style="left:460px;top:2212px"><svg width="40" height="40" viewBox="0 0 40 40" fill="none" stroke="#141b4d" stroke-width="2.5"><rect x="4" y="13" width="32" height="22" rx="2"/><path d="M14 13V8h12v5"/></svg>BUSINESS</div>
<div class="industry-tile abs" style="left:632px;top:2212px"><svg width="40" height="40" viewBox="0 0 40 40" fill="none" stroke="#141b4d" stroke-width="2.5"><rect x="6" y="6" width="28" height="28" rx="3"/><path d="M20 12v16M12 20h16"/></svg>HEALTHCARE</div>
<div class="industry-tile abs" style="left:800px;top:2212px"><svg width="40" height="40" viewBox="0 0 40 40" fill="none" stroke="#141b4d" stroke-width="2.5"><path d="M20 4v8M16 8h8M8 36V20l12-8 12 8v16z"/><rect x="17" y="26" width="6" height="10"/></svg>CHURCHES</div>
<div class="industry-bar abs" style="left:280px;top:2368px"></div>
<div class="industry-bar abs" style="left:460px;top:2368px"></div>
<div class="industry-bar abs" style="left:632px;top:2368px"></div>
<div class="industry-bar abs" style="left:800px;top:2368px"></div>

<div class="industry-tile abs" style="left:280px;top:2388px"><svg width="40" height="40" viewBox="0 0 40 40" fill="none" stroke="#141b4d" stroke-width="2.5"><rect x="8" y="6" width="24" height="30" rx="2"/><path d="M20 12v14M14 17h12"/></svg>RELIGIOUS</div>
<div class="industry-tile abs" style="left:460px;top:2388px"><svg width="40" height="40" viewBox="0 0 40 40" fill="none" stroke="#141b4d" stroke-width="2.5"><path d="M4 16L20 6l16 10M8 16v18h24V16M4 34h32"/><line x1="14" y1="20" x2="14" y2="30"/><line x1="20" y1="20" x2="20" y2="30"/><line x1="26" y1="20" x2="26" y2="30"/></svg>NON-PROFITS</div>
<div class="industry-tile abs" style="left:632px;top:2388px"><svg width="40" height="40" viewBox="0 0 40 40" fill="none" stroke="#141b4d" stroke-width="2.5"><path d="M4 36V18l10 6v-6l10 6v-6l10 6v12zM30 18V6h4v12"/></svg>MANUFACTURING</div>
<div class="industry-tile abs" style="left:800px;top:2388px"><svg width="40" height="40" viewBox="0 0 40 40" fill="none" stroke="#141b4d" stroke-width="2.5"><path d="M4 8h6l4 18h18l4-12H12"/><circle cx="16" cy="32" r="2.5"/><circle cx="29" cy="32" r="2.5"/></svg>RETAIL</div>
<div class="industry-bar abs" style="left:280px;top:2544px"></div>
<div class="industry-bar abs" style="left:460px;top:2544px"></div>
<div class="industry-bar abs" style="left:632px;top:2544px"></div>
<div class="industry-bar abs" style="left:800px;top:2544px"></div>

<div class="people-photo abs" role="img" aria-label="Photo of a seated businessman holding papers in a studio"></div>
<div class="people-box abs">
  <h2>We Know People.</h2>
  <p>Lorem Ipsum is simply dummy text of the printing and typesetting industry. Lorem Ipsum has been the industry's standard dummy text ever since the 1500s.</p>
  <span class="btn-white">Learn More</span>
</div>

<footer class="site-footer abs">
  <div class="abs" style="left:140px;top:70px;text-align:center">
    <div class="f-head">Call Us</div>
    <div class="f-text" style="margin-top:6px">000-0000-0000</div>
    <div class="f-head" style="margin-top:28px">Email Us</div>
    <div class="f-text" style="margin-top:6px">hello@cobaltkin.example</div>
  </div>
  <div class="abs" style="left:340px;top:70px">
    <div class="f-head">For Candiate</div>
    <ul class="f-list"><li>My Resume</li><li>My Profiles</li><li>Favorite Jobs</li><li>Jobs Listing</li><li>Companies</li></ul>
  </div>
  <div class="abs" style="left:580px;top:70px">
    <div class="f-head">For Employer</div>
    <ul class="f-list"><li>Company Profiles</li><li>Manage Jobs</li><li>Resumes Shortlist</li><li>Manage Applications</li><li>Post a new Job</li></ul>
  </div>
  <div class="abs" style="left:828px;top:70px;width:250px">
    <div class="f-head">Contact Us</div>
    <p class="f-text" style="margin-top:14px">Lorem Ipsum is simply dummy text of the printing and typesetting industry. Lorem Ipsum has been the industry's standard dummy text ever since the 1500s, when an unknown printer took.</p>
  </div>
  <div class="brand light abs" style="left:110px;top:262px"><span class="dot"></span>Cobalt Kin</div>
</footer>
<div class="footer-bottom abs" style="color:var(--white)">
  <span>© 2022 Cobalt Kin – ALL RIGHTS RESERVED. PRIVACY POLICY</span>
  <div class="socials"><span></span><span></span><span></span><span></span></div>
</div>

</body>
</html>
```